Industrial Design Business Card

I am an industrial designer that needs a nice business card that gives a sense of my personal brand (the work I do, how I'm different than others though subtle design). Since I am a designer, myself, the business card needs to have an impeccable design, while feeling like it represents me. Please see the link to my portfolio where you can get a better sense for me.

http://www.markdpelletier.example/

Target Market(s)

Potential employers, industrial designers

Industry/Entity Type

Business

Contact Information for Business Card

Mark Pelletier
Industrial Designer
markpelletierdesign.example
markpelletierdesign@mailbox.example
(555) 218-4370

Font styles to use
Sans Serif

Colors

Designer to choose colors to be used in the design.

Requirements
Must have
• Must have all of the business card details - ideally in that order. If it will look better in a different order, that's fine.
• Simple design - not too flashy. Using a font that is not a pre-set will likely be key to making this simple but also stand out. But also keep somewhat consistent with the fonts and look of my portfolio (markpelletierdesign.example).
• It needs to catch someone's attention while also being simple (not too flashy) design. That is the big challenge.
Should not have
• Random pictures off the internet.

```html
<!DOCTYPE html>
<html lang="en">
<head>
<meta charset="utf-8">
<title>Mark Pelletier — Business Card</title>
<link href="https://fonts.googleapis.com/css2?family=Arimo:wght@400;700&display=swap" rel="stylesheet">
<style>
  :root {
    --backdrop: #ececec;
    --paper: #ffffff;
    --ink: #111111;
    --ink-soft: #333333;
    --night: #000000;
    --accent: #f2a71b;
  }
  * { margin: 0; padding: 0; box-sizing: border-box; }
  html, body {
    width: 1200px; height: 900px; overflow: hidden;
    background: var(--backdrop);
    font-family: "Arimo", Arial, sans-serif;
  }
  .stage {
    width: 1200px; height: 900px;
    display: flex; align-items: center; justify-content: center; gap: 50px;
  }
  .card {
    position: relative;
    width: 500px; height: 286px;
    box-shadow: 0 6px 18px rgba(0,0,0,0.12);
  }
  .card--front { background: var(--paper); color: var(--ink); }
  .card--back { background: var(--night); color: #fff; }

  .identity { position: absolute; left: 34px; top: 30px; }
  .identity__name { font-weight: 700; font-size: 15px; letter-spacing: 0.3px; text-transform: uppercase; }
  .identity__role { font-size: 13px; color: var(--accent); margin-top: 3px; }

  .contacts {
    position: absolute; left: 34px; top: 128px;
    list-style: none; font-size: 13px; color: var(--ink-soft); line-height: 18px;
  }
  .contacts__item { display: flex; align-items: center; gap: 7px; }
  .contacts__icon { width: 10px; height: 10px; flex: none; fill: var(--ink-soft); }

  .wordmark {
    position: absolute; display: flex; align-items: center; gap: 12px;
    font-size: 22px; font-weight: 400; letter-spacing: 1.5px; text-transform: uppercase;
  }
  .wordmark__square { width: 14px; height: 14px; flex: none; }
  .card--front .wordmark { right: 32px; bottom: 42px; color: var(--ink); }
  .card--front .wordmark__square { background: var(--accent); }
  .card--back .wordmark {
    left: 50%; top: 50%; transform: translate(-50%, -50%);
    color: #fff; white-space: nowrap;
  }
  .card--back .wordmark__square { background: var(--accent); }
</style>
</head>
<body>
  <main class="stage">
    <section class="card card--front" aria-label="Business card front">
      <div class="identity">
        <p class="identity__name">Mark Pelletier</p>
        <p class="identity__role">Industrial Designer</p>
      </div>
      <ul class="contacts">
        <li class="contacts__item">
          <svg class="contacts__icon" viewBox="0 0 10 10" aria-hidden="true"><path d="M2 0.5h2l0.8 2.2-1.2 0.9a6 6 0 0 0 2.8 2.8l0.9-1.2 2.2 0.8v2a1 1 0 0 1-1 1A8.5 8.5 0 0 1 1 1.5a1 1 0 0 1 1-1z"/></svg>
          (555) 218-4370
        </li>
        <li class="contacts__item">
          <svg class="contacts__icon" viewBox="0 0 10 10" aria-hidden="true"><path d="M0.5 2h9v6h-9z M0.5 2l4.5 3.5 4.5-3.5" fill="none" stroke="#333" stroke-width="1"/></svg>
          markpelletierdesign@mailbox.example
        </li>
        <li class="contacts__item">
          <svg class="contacts__icon" viewBox="0 0 10 10" aria-hidden="true"><circle cx="5" cy="5" r="4.5"/></svg>
          markpelletierdesign.example
        </li>
      </ul>
      <div class="wordmark">
        <span class="wordmark__square" aria-hidden="true"></span>
        Mark Pelletier
      </div>
    </section>

    <section class="card card--back" aria-label="Business card back">
      <div class="wordmark">
        <span class="wordmark__square" aria-hidden="true"></span>
        Mark Pelletier
      </div>
    </section>
  </main>
</body>
</html>
```